Presentation Folder, Business Card, Letterhead and Envelope design

We are a dental clinic that will open in August and we are looking for a professional graphic designer to create our Business Card, Presentation Folder, Letterhead, Notepad and envelopes.

The brand NovaGrin must reflect a sense of quality and sophistication, marketed for middle-class consumers.
Our preference is for quality and refined materials, where less is more.
Attached the logo

```html
<!DOCTYPE html>
<html lang="en">
<head>
<meta charset="utf-8">
<title>NovaGrin — Presentation Folder</title>
<link href="https://fonts.googleapis.com/css2?family=Montserrat:wght@300;400&display=swap" rel="stylesheet">
<style>
  :root {
    --backdrop: #b9b9b9;
    --paper: #f6f6f6;
    --paper-shade: #e4e4e4;
    --burgundy: #600d0f;
    --burgundy-light: #7a2326;
    --ink: #4a4a4a;
    --white: #ffffff;
  }
  * { box-sizing: border-box; margin: 0; padding: 0; }
  html, body { width: 842px; height: 1200px; overflow: hidden; }
  body {
    background: var(--backdrop);
    font-family: "Montserrat", sans-serif;
    position: relative;
  }
  .spread {
    position: absolute;
    left: 51px;
    width: 740px;
    height: 500px;
    display: flex;
    box-shadow: 0 10px 28px rgba(0,0,0,0.25);
  }
  .spread--outside { top: 50px; }
  .spread--inside { top: 640px; }
  .panel {
    position: relative;
    width: 370px;
    height: 500px;
    overflow: hidden;
  }
  .panel--back {
    background: linear-gradient(120deg, var(--paper-shade), var(--paper) 40%, var(--paper-shade));
  }
  .panel--front {
    background: linear-gradient(135deg, var(--burgundy-light), var(--burgundy) 45%);
  }
  .fold-line {
    position: absolute;
    top: 0;
    bottom: 0;
    left: 318px;
    width: 1px;
    background: rgba(255,255,255,0.8);
  }
  .wordmark {
    position: absolute;
    display: flex;
    align-items: center;
    gap: 10px;
    color: var(--white);
    font-weight: 300;
    letter-spacing: 0.22em;
    text-transform: uppercase;
  }
  .wordmark__square {
    width: 18px;
    height: 18px;
    background: var(--white);
  }
  .panel--front .wordmark {
    top: 196px;
    left: 70px;
    font-size: 24px;
  }
  .contact {
    position: absolute;
    left: 0;
    right: 0;
    bottom: 48px;
    text-align: center;
    color: var(--ink);
    font-size: 8.5px;
    line-height: 1.6;
    font-weight: 400;
  }
  .contact__name {
    color: var(--burgundy);
    font-size: 13px;
    letter-spacing: 0.22em;
    text-transform: uppercase;
    font-weight: 300;
    margin-bottom: 8px;
  }
  .contact__row { display: flex; justify-content: center; gap: 10px; align-items: center; }
  .contact__item { display: inline-flex; align-items: center; gap: 3px; }
  .contact__item svg { width: 8px; height: 8px; fill: var(--burgundy); }
  .contact__web { color: var(--burgundy); }
  .panel--inside {
    background: linear-gradient(160deg, var(--white), var(--paper) 60%, var(--paper-shade));
  }
  .panel--inside + .panel--inside { border-left: 1px solid #dcdcdc; }
  .pocket {
    position: absolute;
    left: 0;
    right: 0;
    bottom: 0;
    height: 190px;
    box-shadow: 0 -3px 8px rgba(0,0,0,0.18);
  }
  .pocket--left {
    background: linear-gradient(90deg, var(--burgundy), var(--burgundy-light));
  }
  .pocket--right {
    background: linear-gradient(90deg, var(--burgundy) 20%, var(--burgundy-light));
  }
  .pocket .wordmark {
    right: 24px;
    bottom: 28px;
    font-size: 17px;
    gap: 8px;
  }
  .pocket .wordmark__square { width: 13px; height: 13px; }
</style>
</head>
<body>
  <section class="spread spread--outside" aria-label="Folder outside">
    <div class="panel panel--back">
      <div class="contact">
        <p class="contact__name">NovaGrin</p>
        <p>Suite 7, 12 Harbour Rd, Seaview, QLD 4300</p>
        <p class="contact__row">
          <span class="contact__item">
            <svg viewBox="0 0 10 10"><path d="M2 0.5 L4 3 L3 4.2 Q4.3 6 5.8 7 L7 6 L9.5 8 L8.3 9.5 Q4 9 0.5 1.7 Z"/></svg>
            07 5550 0142
          </span>
          <span class="contact__item">
            <svg viewBox="0 0 10 10"><rect x="0.5" y="2" width="9" height="6.5"/><path d="M0.5 2 L5 5.5 L9.5 2" stroke="#fff" stroke-width="0.8" fill="none"/></svg>
            contact@novagrin.com.au
          </span>
        </p>
        <p class="contact__web">www.novagrin.com.au</p>
      </div>
    </div>
    <div class="panel panel--front">
      <div class="fold-line"></div>
      <div class="wordmark"><span class="wordmark__square"></span>NovaGrin</div>
    </div>
  </section>

  <section class="spread spread--inside" aria-label="Folder inside">
    <div class="panel panel--inside">
      <div class="pocket pocket--left"></div>
    </div>
    <div class="panel panel--inside">
      <div class="pocket pocket--right">
        <div class="wordmark"><span class="wordmark__square"></span>NovaGrin</div>
      </div>
    </div>
  </section>
</body>
</html>
```